Orlent Telecom Business Card Competition

High quality international communications for consumers and business. We are re-designing our website and re-branding. Our current (old) website can be viewed at www.goorlent-example.net Vision statement - We enable people and communities to build and maintain strong and lasting global connections This is the brand image that we are trying to get across: •Quality—Orlent delivers the highest quality connections wherever you need to communicate. •Service—Orlent is always there for you, with the industry-leading service that promises to ensure that every experience is a good one. •Value—Orlent provides the best value in the global communications market. Typical messaging: Connecting the Most Important People in the World. Focus on international communications

We want to convey our service quality and that we really care about the service we provide and our customers. We want to emphasis the international aspect of our business. We want to make it personal, but it has to relate to business as well as individuals. We want the card to be unique in design but clear enough to read. We want a business prospect as well as a regular person to look at our card and know what we do.

Target Market(s)

Consumer - multi-ethnic consumer base living in the US calling, texting and connecting with family and friends in countries around the world 2. Busine

Industry/Entity Type

Communications

Requirements
Must have
• 1. Logo must be visible (see uploaded)

2.Artist can use variations of our company colors to accent our logo:

Hex Codes:
Magenta = ab3179
Blue = 2895c0
Green = 8ebb3f

3.Must have the following slogan visible: Because Every Connection Counts

below are the required data fields:

Full Name: Mark Tallow
Position: Chief Financial Officer
Office: +1 608-441-2871 ext.318
Mobile: +1 608-441-2871
Fax: +1 608-441-2871
Email: MarkT@goorlent-example.net
URL: www.goorlent-example.net
Address:
71820 Brindle Avenue
suite 412
Carrow Falls, NE 20163
USA

Nice to have
• Die cut cards or uniquely shaped cards would be interesting to see but not required

```html
<!DOCTYPE html>
<html lang="en">
<head>
<meta charset="utf-8">
<title>Orlent Telecom – Business Card</title>
<link rel="stylesheet" href="https://fonts.googleapis.com/css2?family=Open+Sans:wght@400;600;700&display=swap">
<style>
  :root {
    --magenta: #ab3179;
    --blue: #2895c0;
    --green: #8ebb3f;
    --yellow: #e8c63a;
    --card-dark: #3a3a3c;
    --card-light: #fbfbfb;
    --ink: #1f1f1f;
    --stage: #d9d9d9;
  }
  * { box-sizing: border-box; margin: 0; padding: 0; }
  html, body { width: 1200px; height: 880px; overflow: hidden; }
  body {
    background: var(--stage);
    font-family: "Open Sans", Arial, sans-serif;
    display: flex;
    flex-direction: column;
    align-items: center;
    justify-content: center;
    gap: 40px;
  }
  .card {
    width: 600px;
    height: 344px;
    border-radius: 26px;
    position: relative;
    overflow: hidden;
  }

  /* Front */
  .card--front {
    background: var(--card-dark);
    display: flex;
    flex-direction: column;
    align-items: center;
    justify-content: center;
    gap: 30px;
  }
  .brand {
    display: flex;
    align-items: center;
    gap: 16px;
  }
  .brand__mark { border-radius: 5px; }
  .brand__name { font-weight: 700; letter-spacing: 0.02em; white-space: nowrap; }
  .card--front .brand__mark { background: var(--magenta); width: 38px; height: 38px; }
  .card--front .brand__name { color: #f2f2f2; font-size: 54px; }
  .slogan {
    background: var(--magenta);
    color: #3a1a2c;
    font-size: 19px;
    border-radius: 6px;
    padding: 5px 0;
    width: 340px;
    text-align: center;
  }

  /* Back */
  .card--back {
    background: var(--card-light);
    padding: 32px 40px;
  }
  .card--back .brand__mark { background: var(--green); width: 24px; height: 24px; }
  .card--back .brand__name { color: var(--blue); font-size: 30px; }
  .contact {
    position: absolute;
    left: 250px;
    top: 96px;
    right: 40px;
    color: var(--ink);
  }
  .contact__name {
    font-size: 20px;
    font-weight: 400;
    letter-spacing: 0.03em;
    text-transform: uppercase;
    line-height: 1.15;
  }
  .contact__title { font-size: 13.5px; margin-top: 1px; }
  .rules { margin: 7px 0 9px; display: grid; gap: 2px; }
  .rules span { display: block; height: 1px; }
  .rules .r1 { background: var(--blue); }
  .rules .r2 { background: var(--magenta); }
  .rules .r3 { background: var(--green); }
  .rules .r4 { background: var(--yellow); }
  .lines { list-style: none; font-size: 13.5px; line-height: 1.35; }
  .lines .label {
    display: inline-block;
    width: 18px;
    font-size: 11px;
    font-weight: 600;
  }
  .label--t { color: var(--blue); }
  .label--m { color: var(--magenta); }
  .label--f { color: var(--green); }
  .label--e { color: var(--blue); }
  .address { font-size: 13.5px; line-height: 1.35; margin-top: 4px; }
  .url { font-size: 13.5px; margin-top: 6px; }
  .url strong { color: var(--blue); font-weight: 700; }
</style>
</head>
<body>
  <section class="card card--front" aria-label="Card front">
    <div class="brand">
      <span class="brand__mark"></span>
      <span class="brand__name">Orlent Telecom</span>
    </div>
    <p class="slogan">Because Every Connection Counts</p>
  </section>

  <section class="card card--back" aria-label="Card back">
    <div class="brand">
      <span class="brand__mark"></span>
      <span class="brand__name">Orlent Telecom</span>
    </div>
    <div class="contact">
      <h1 class="contact__name">Mark Tallow</h1>
      <p class="contact__title">Chief Financial Officer</p>
      <div class="rules"><span class="r1"></span><span class="r2"></span><span class="r3"></span><span class="r4"></span></div>
      <ul class="lines">
        <li><span class="label label--t">T</span>+1 608-441-2871 ext.318</li>
        <li><span class="label label--m">M</span>+1 608-441-2871</li>
        <li><span class="label label--f">F</span>+1 608-441-2871</li>
        <li><span class="label label--e">E</span>MarkT@goorlent-example.net</li>
      </ul>
      <p class="address">71820 Brindle Avenue, suite 412<br>Carrow Falls, NE 20163 USA</p>
      <p class="url">www.<strong>goorlent-example</strong>.net</p>
    </div>
  </section>
</body>
</html>
```